Business Card Design for Cybersecurity Company - Quorvent Systems

We need a business card design for our new cybersecurity company, Quorvent. We’re going for a clean, hi tech look that feels modern, premium, and trustworthy. We want a design that really stands out and makes people say WOW when we hand it over!

Quorvent delivers reliable IT support and managed services for small and mid sized businesses. We help companies stay secure, efficient, and connected through proactive monitoring, cybersecurity services, cloud management, and remote support.

Target Market(s)

Designers should target small and mid sized businesses that need dependable cybersecurity and IT support.

Industry/Entity Type

Cybersecurity, Managed Service Provider, IT services

Contact Information for Business Card

Contact information

Requirements
Must have
• The card should look clean, modern, and tech focused, with the Quorvent logo, clear contact info, and strong readability. It needs to feel premium and professional while still keeping a simple layout that fits a cybersecurity and IT brand.
Nice to have
• Nice to have elements include subtle touches that give the card a modern, tech feel, along with a layout that works well in different background styles.
Should not have
• The card should avoid clutter, loud graphics, or anything that takes attention away from the logo and contact details.

```html
<!DOCTYPE html>
<html lang="en">
<head>
<meta charset="utf-8">
<title>Quorvent Systems – Business Card</title>
<link rel="stylesheet" href="https://fonts.googleapis.com/css2?family=Montserrat:wght@300;400;500;700&display=swap">
<style>
  :root {
    --stage: #161616;
    --card-light: #f4f4f4;
    --card-dark: #1f1f1f;
    --brand-blue: #3f78c4;
    --brand-purple: #6a4aa6;
    --brand-mark: #4d5db5;
    --ink: #222226;
    --emboss: #2b2b2b;
    --white: #ffffff;
  }
  * { margin: 0; padding: 0; box-sizing: border-box; }
  html, body { width: 1200px; height: 1059px; overflow: hidden; }
  body {
    background: var(--stage);
    font-family: "Montserrat", sans-serif;
    position: relative;
  }
  .card {
    position: absolute;
    border-radius: 18px;
    overflow: hidden;
  }
  .card--front {
    left: 256px; top: 89px; width: 688px; height: 390px;
    background: var(--card-light);
  }
  .card--back {
    left: 254px; top: 547px; width: 693px; height: 393px;
    background: var(--card-dark);
  }
  .name-band {
    position: absolute;
    left: 0; top: 51px; width: 440px; height: 78px;
    background: linear-gradient(90deg, var(--brand-blue), var(--brand-purple));
  }
  .person-name {
    position: absolute; left: 40px; top: 15px;
    color: var(--white); font-weight: 700; font-size: 24px; letter-spacing: 0.2px;
  }
  .person-title {
    position: absolute; left: 40px; top: 45px;
    color: var(--white); font-weight: 300; font-size: 16.5px; white-space: nowrap;
  }
  .brand-dot {
    position: absolute; left: 408px; top: 54px;
    width: 72px; height: 72px; border-radius: 50%;
    background: var(--brand-purple);
  }
  .brand-name {
    position: absolute; left: 492px; top: 69px;
    color: var(--brand-mark); font-weight: 500; font-size: 32px; line-height: 40px;
  }
  .vanity-number {
    position: absolute; left: 40px; top: 218px;
    color: var(--brand-blue); font-weight: 500; font-size: 21px;
  }
  .contact-list {
    position: absolute; left: 39px; top: 252px; list-style: none;
  }
  .contact-list li {
    display: flex; align-items: center; height: 26px;
    color: var(--ink); font-size: 18px; font-weight: 400;
  }
  .contact-list svg { width: 14px; height: 14px; margin-right: 7px; fill: var(--brand-blue); }
  .back-brand {
    position: absolute; left: 0; right: 0; top: 150px;
    display: flex; align-items: center; justify-content: center; gap: 22px;
  }
  .back-brand__dot { width: 84px; height: 84px; border-radius: 50%; background: var(--emboss); }
  .back-brand__name { color: var(--emboss); font-weight: 500; font-size: 58px; }
</style>
</head>
<body>
  <section class="card card--front">
    <div class="name-band">
      <div class="person-name">DANA WHITCOMBE</div>
      <div class="person-title">Owner | CEO | Quorvent Systems</div>
    </div>
    <div class="brand-dot"></div>
    <div class="brand-name">Quorvent</div>

    <div class="vanity-number">(855) 555-QRVT</div>
    <ul class="contact-list">
      <li><svg viewBox="0 0 24 24"><path d="M6.6 10.8a15 15 0 0 0 6.6 6.6l2.2-2.2c.3-.3.7-.4 1-.2 1.1.4 2.3.6 3.6.6.6 0 1 .4 1 1V20c0 .6-.4 1-1 1A17 17 0 0 1 3 4c0-.6.4-1 1-1h3.5c.6 0 1 .4 1 1 0 1.3.2 2.5.6 3.6.1.3 0 .7-.2 1z"/></svg>(855) 555 7788</li>
      <li><svg viewBox="0 0 24 24"><path d="M7 1h10a2 2 0 0 1 2 2v18a2 2 0 0 1-2 2H7a2 2 0 0 1-2-2V3a2 2 0 0 1 2-2zm0 3v14h10V4zm5 15.5a1.2 1.2 0 1 0 0 2.4 1.2 1.2 0 0 0 0-2.4z"/></svg>(813) 555-0142</li>
      <li><svg viewBox="0 0 24 24"><path d="M2 5h20v14H2zm2 2v.4l8 5.3 8-5.3V7zm0 2.8V17h16V9.8l-8 5.3z"/></svg>dana@quorvent.com</li>
      <li><svg viewBox="0 0 24 24"><path d="M12 2a10 10 0 1 0 0 20 10 10 0 0 0 0-20zm6.9 9h-3a15 15 0 0 0-1.2-6.2A8 8 0 0 1 18.9 11zM12 4c.9 1.2 1.7 3.8 1.9 7h-3.8c.2-3.2 1-5.8 1.9-7zM9.3 4.8A15 15 0 0 0 8.1 11h-3a8 8 0 0 1 4.2-6.2zM5.1 13h3a15 15 0 0 0 1.2 6.2A8 8 0 0 1 5.1 13zM12 20c-.9-1.2-1.7-3.8-1.9-7h3.8c-.2 3.2-1 5.8-1.9 7zm2.7-.8a15 15 0 0 0 1.2-6.2h3a8 8 0 0 1-4.2 6.2z"/></svg>www.quorvent.com</li>
    </ul>
  </section>

  <section class="card card--back">
    <div class="back-brand">
      <div class="back-brand__dot"></div>
      <div class="back-brand__name">Quorvent</div>
    </div>
  </section>
</body>
</html>
```